This is for a poster that will be hanging in the window of a Men's Suit Store in the mall:
Size 4 feet wide by 6 feet high
Main point is: A sale on "Suits" or "Men's Suits" at 40%-60% off ( the 40%-60% off should be the focal point)
Some words that can be used are "Sale" or "Clearance Sale"
Some key words that can be used to make it urgent are "limited time offer" or something similar.
You can get creative, the point is for the customer to want to come into the store and buy a suit right away.
You may use a graphic (picture of a man in a suit). It is not necessary but if it looks good you can use it. (If you do use a picture, it should be of a modern fit or slim fit suit)
Sorry, the initial brief somehow got deleted from the project. Please see the updated brief.
Thanks
Reason: Project was closed for some reason, extended to give enough time to complete
Mostly Men ages 35-55
Store
Designer to choose colors to be used in the design.

```html
<!DOCTYPE html>
<html lang="en">
<head>
<meta charset="UTF-8">
<title>Suits Sale Poster</title>
<link rel="stylesheet" href="https://fonts.googleapis.com/css2?family=Poppins:wght@600&family=Libre+Franklin:wght@700&display=swap">
<style>
  :root {
    --page-bg: #ffffff;
    --red-deep: #c20000;
    --red-bright: #ff0404;
    --red-mid: #d90000;
    --type-light: #ffffff;
    --type-shade: #d6d6d6;
  }
  html, body {
    margin: 0;
    padding: 0;
    width: 1200px;
    height: 1000px;
    overflow: hidden;
    background: var(--page-bg);
  }
  .canvas {
    display: block;
    width: 1200px;
    height: 1000px;
  }
  .headline { font-family: "Poppins", "Century Gothic", sans-serif; font-weight: 600; }
  .tagline { font-family: "Libre Franklin", "Franklin Gothic Medium", sans-serif; font-weight: 700; }
  .bg-deep { stop-color: var(--red-deep); }
  .bg-bright { stop-color: var(--red-bright); }
  .bg-mid { stop-color: var(--red-mid); }
  .type-light { stop-color: var(--type-light); }
  .type-shade { stop-color: var(--type-shade); }
</style>
</head>
<body>
<svg class="canvas" viewBox="0 0 1200 1000" xmlns="http://www.w3.org/2000/svg" aria-label="Suits sale poster, 40% to 60% off">
  <defs>
    <linearGradient id="poster-fill" x1="1" y1="0" x2="0" y2="1">
      <stop offset="0" class="bg-deep"/>
      <stop offset="0.4" class="bg-bright"/>
      <stop offset="0.78" class="bg-mid"/>
      <stop offset="1" class="bg-bright"/>
    </linearGradient>
    <linearGradient id="type-fill" x1="0" y1="0" x2="0" y2="1">
      <stop offset="0" class="type-light"/>
      <stop offset="0.45" class="type-light"/>
      <stop offset="1" class="type-shade"/>
    </linearGradient>
  </defs>

  <rect class="poster" x="351" y="131" width="499" height="738" fill="url(#poster-fill)"/>

  <g class="poster-copy" fill="url(#type-fill)">
    <text class="headline sale-word" x="383" y="316" font-size="218" textLength="440" lengthAdjust="spacingAndGlyphs">SALE</text>
    <text class="headline product-word" x="605" y="405" font-size="112" textLength="223" lengthAdjust="spacingAndGlyphs">Suits</text>
    <text class="headline discount-low" x="369" y="553" font-size="178" textLength="327" lengthAdjust="spacingAndGlyphs">40%</text>
    <text class="headline discount-high" x="508" y="712" font-size="182" textLength="324" lengthAdjust="spacingAndGlyphs">60%</text>
    <text class="headline off-word" x="690" y="788" font-size="84" textLength="139" lengthAdjust="spacingAndGlyphs">OFF</text>
    <text class="tagline urgency-line" x="381" y="854" font-size="52" textLength="437" lengthAdjust="spacingAndGlyphs">Hurry Limited Time</text>
  </g>
</svg>
</body>
</html>
```